Modern Design Business Card industrial maintenance company

Business card design for Company named Brookvale Equipment Services

Target Market(s)

Industrial

Industry/Entity Type

Maintenance and repair

Contact Information for Business Card

Place holder for address, office phone, mobile number and email

Requirements
Must have
• Clean modern look
Nice to have
• N/a

```html
<!DOCTYPE html>
<html lang="en">
<head>
<meta charset="utf-8">
<title>Brookvale Equipment Services – Business Card</title>
<link href="https://fonts.googleapis.com/css2?family=Montserrat:wght@400;500;600;700&display=swap" rel="stylesheet">
<style>
  :root {
    --backdrop: #2e2e2e;
    --card-black: #1c1c1c;
    --card-white: #ffffff;
    --ink-dark: #141414;
    --silver: #bdbdbd;
    --silver-light: #e4e4e4;
    --silver-dark: #8a8a8a;
    --text-light: #dedede;
  }
  * { box-sizing: border-box; margin: 0; padding: 0; }
  html, body {
    width: 1200px; height: 1200px; overflow: hidden;
    background: var(--backdrop);
    font-family: "Montserrat", sans-serif;
  }
  .canvas {
    width: 1200px; height: 1200px;
    display: flex; flex-direction: column; align-items: center; justify-content: center;
    gap: 60px;
  }
  .card {
    width: 900px; height: 514px;
    border-radius: 38px;
    overflow: hidden;
    position: relative;
    box-shadow: 0 14px 30px rgba(0,0,0,.45);
  }

  /* Front */
  .card--front { background: var(--card-black); }
  .front__top {
    position: absolute; left: 0; top: 0; width: 100%; height: 236px;
    background: var(--card-white);
    display: flex; align-items: center; padding-left: 110px; gap: 28px;
  }
  .front__band {
    position: absolute; left: 0; top: 250px; width: 100%; height: 12px;
    background: linear-gradient(90deg, var(--silver-dark), var(--silver-light) 50%, var(--silver));
  }
  .brand-mark {
    width: 112px; height: 112px; border-radius: 50%;
    border: 6px solid var(--ink-dark); flex: none;
  }
  .brand-name {
    font-weight: 600; font-size: 34px; letter-spacing: 3px;
    text-transform: uppercase; color: var(--ink-dark); line-height: 1.2;
  }
  .person {
    position: absolute; left: 110px; top: 340px; color: var(--text-light);
  }
  .person__name { font-weight: 700; font-size: 44px; letter-spacing: 1px; line-height: 1.05; }
  .person__role { font-weight: 500; font-size: 24px; letter-spacing: 1px; color: var(--silver); }
  .contact {
    position: absolute; left: 520px; top: 290px;
    list-style: none; color: var(--text-light); font-size: 22px; line-height: 1.2;
  }
  .contact li { display: flex; align-items: flex-start; gap: 12px; margin-bottom: 8px; }
  .contact svg { width: 22px; height: 22px; flex: none; margin-top: 2px; fill: var(--text-light); }

  /* Back */
  .card--back {
    background: var(--card-black);
    display: flex; flex-direction: column; align-items: center; justify-content: center; gap: 34px;
  }
  .card--back .brand-mark { width: 190px; height: 190px; border: 8px solid var(--silver); }
  .card--back .brand-name { color: var(--silver); font-size: 40px; letter-spacing: 4px; text-align: center; }
</style>
</head>
<body>
<main class="canvas">
  <section class="card card--front" aria-label="Business card front">
    <div class="front__top">
      <span class="brand-mark" aria-hidden="true"></span>
      <p class="brand-name">Brookvale<br>Equipment Services</p>
    </div>
    <div class="front__band"></div>
    <div class="person">
      <p class="person__name">FULL NAME</p>
      <p class="person__role">POSITION</p>
    </div>
    <ul class="contact">
      <li><svg viewBox="0 0 24 24"><path d="M6.6 10.8a15 15 0 0 0 6.6 6.6l2.2-2.2a1 1 0 0 1 1-.25 11.4 11.4 0 0 0 3.6.57 1 1 0 0 1 1 1V20a1 1 0 0 1-1 1A17 17 0 0 1 3 4a1 1 0 0 1 1-1h3.5a1 1 0 0 1 1 1c0 1.25.2 2.45.57 3.57a1 1 0 0 1-.25 1z"/></svg>(000) 000 0000</li>
      <li><svg viewBox="0 0 24 24"><path d="M7 1h10a2 2 0 0 1 2 2v18a2 2 0 0 1-2 2H7a2 2 0 0 1-2-2V3a2 2 0 0 1 2-2zm0 3v14h10V4zm5 15.5a1 1 0 1 0 0 2 1 1 0 0 0 0-2z"/></svg>(000) 000 0000</li>
      <li><svg viewBox="0 0 24 24"><path d="M2 5h20v14H2zm2 2v.5l8 5 8-5V7zm0 2.9V17h16V9.9l-8 5z"/></svg>email@brookvaleservices.com</li>
      <li><svg viewBox="0 0 24 24"><path d="M12 2a7 7 0 0 1 7 7c0 5-7 13-7 13S5 14 5 9a7 7 0 0 1 7-7zm0 4.5a2.5 2.5 0 1 0 0 5 2.5 2.5 0 0 0 0-5z"/></svg><span>123 Name Street, 000<br>Your City, 00000-000</span></li>
    </ul>
  </section>

  <section class="card card--back" aria-label="Business card back">
    <span class="brand-mark" aria-hidden="true"></span>
    <p class="brand-name">Brookvale<br>Equipment Services</p>
  </section>
</main>
</body>
</html>
```